Hi, Looking for an upgraded business card to the aged one attached. Open to suggestions and no real limitations, but if your going to use a picture of a taxi i think it should be vector based rather than a full color picture. I've uploaded a 2 pictures of the type of taxi which is a Velmora K7 in white. The taxi markings look like the pink one in the picture but to be clear his is white. The taxi is in Bermuda so if you wanted to include something island based that's ok as well but not required. The other thing he wanted to keep on there was the bermuda police crest, with the retired police office incorporated somehow.

Requirements
Must have
• Bermuda Taxi Operator
Retired Police Officer
Police Crest
Taxi #
Email
Mobile Number

```html
<!DOCTYPE html>
<html lang="en">
<head>
<meta charset="utf-8">
<title>Bermuda Taxi Operator – Business Card</title>
<link rel="stylesheet" href="https://fonts.googleapis.com/css2?family=Arimo:wght@700&family=Jost:ital,wght@0,400;0,500;1,400&display=swap">
<style>
  :root {
    --page-bg: #ffffff;
    --card-bg: #ffffff;
    --navy: #0f4a7e;
    --royal: #0d67c9;
    --ink: #111111;
    --sky-top: #c9dcef;
    --sky-bottom: #e9eef3;
    --street: #8e8f93;
    --shadow: rgba(0, 0, 0, 0.22);
  }
  * { margin: 0; padding: 0; box-sizing: border-box; }
  html, body {
    width: 1200px; height: 1200px; overflow: hidden;
    background: var(--page-bg);
  }
  .business-card {
    position: absolute;
    left: 169px; top: 354px;
    width: 862px; height: 492px;
    background: var(--card-bg);
    box-shadow: 0 0 14px var(--shadow);
    overflow: hidden;
  }
  .card-art {
    position: absolute; inset: 0;
    width: 862px; height: 492px;
  }
  .crest-mark {
    position: absolute;
    left: 58px; top: 70px;
    width: 150px;
    display: flex; flex-direction: column; align-items: center; gap: 10px;
  }
  .crest-mark__dot {
    width: 70px; height: 70px; border-radius: 50%;
    background: var(--navy);
  }
  .crest-mark__name {
    font-family: "Jost", sans-serif;
    font-weight: 500;
    font-size: 17px;
    line-height: 1.15;
    color: var(--navy);
    text-align: center;
  }
  .card-title {
    position: absolute;
    left: 245px; top: 52px;
    font-family: "Arimo", sans-serif;
    font-weight: 700;
    font-size: 38px;
    letter-spacing: 1px;
    color: var(--navy);
    white-space: nowrap;
  }
  .holder-name {
    position: absolute;
    left: 66px; top: 220px;
    font-family: "Jost", sans-serif;
    font-weight: 400;
    font-size: 38px;
    color: var(--navy);
    line-height: 1;
  }
  .holder-role {
    position: absolute;
    left: 66px; top: 266px;
    font-family: "Jost", sans-serif;
    font-style: italic;
    font-size: 30px;
    color: var(--ink);
    line-height: 1;
  }
  .contact {
    position: absolute;
    left: 66px; top: 372px;
    font-family: "Jost", sans-serif;
    font-size: 27px;
    line-height: 30px;
    color: var(--ink);
  }
  .taxi-number {
    position: absolute;
    left: 572px; top: 431px;
    width: 290px; height: 61px;
    background: var(--royal);
    color: #ffffff;
    font-family: "Arimo", sans-serif;
    font-weight: 700;
    font-size: 34px;
    display: flex; align-items: center; justify-content: center;
    letter-spacing: 0.5px;
  }
</style>
</head>
<body>
  <div class="business-card">
    <svg class="card-art" viewBox="0 0 862 492" xmlns="http://www.w3.org/2000/svg">
      <defs>
        <linearGradient id="street-scene" x1="0" y1="0" x2="0" y2="1">
          <stop offset="0" stop-color="var(--sky-top)"/>
          <stop offset="0.35" stop-color="var(--sky-bottom)"/>
          <stop offset="0.6" stop-color="#d9a7b8"/>
          <stop offset="1" stop-color="var(--street)"/>
        </linearGradient>
      </defs>
      <path class="arc-band" d="M388 492 C395 330 560 150 780 145 Q830 147 862 163 L862 492 Z" fill="var(--royal)"/>
      <path class="street-photo" role="img" aria-label="Photo of a pink taxi van parked on a Bermuda harbourfront street lined with pastel shops"
            d="M398 492 C420 360 570 225 760 222 Q830 224 862 234 L862 492 Z" fill="url(#street-scene)"/>
    </svg>

    <div class="crest-mark">
      <span class="crest-mark__dot"></span>
      <span class="crest-mark__name">Harbour Constabulary</span>
    </div>

    <h1 class="card-title">BERMUDA TAXI OPERATOR</h1>

    <p class="holder-name">Dorian Quell</p>
    <p class="holder-role">Retired Police Officer</p>

    <p class="contact">
      <span class="contact__email">dquell208@mailbox.example</span><br>
      <span class="contact__phone">1-441-555-0142</span>
    </p>

    <div class="taxi-number">Taxi # T2481</div>
  </div>
</body>
</html>
```